Brightpath EAP 2 x Flyer with Poster

Brightpath is an award-winning organisation providing dynamic and creative ways for children, young people, adults and families to make positive change and achieve fulfilling lives.
We are launching into a new area of business and starting to offer organisations Employee Assistance Program (EAP). To launch this service we need 2 flyers and a poster:
- 1 x flyer for employers
- 1 x flyer for employees
- 1 x poster (A3) for employees to be displayed around the office.
For the flyers we are after an a4 colour double sided flyer in either a A4 tri-fold to DL format or A4 bi-fold to A5 format. We are looking for a design that is simple and dynamic whilst keeping in line with our branding.
The winning designs will need to be hi-res and ready for print and also a lower res version suitable to email.
I have attached a number of files to provide further background, including:
• I have attached 3 x word doc of copy for each (2 x flyer / 1 x poster)
• Brand Guidelines
• Logo
• Our clinic flyer recently produced by a ArtHive designer for our clinic area of the business. These flyers do not have to be exactly the same as this one but should appear to be from the same organisation although a different service.
Generally we like our designs to be clear and simple.
Please don't hesitate to reach out with any Q's.

```html
<!DOCTYPE html>
<html lang="en">
<head>
<meta charset="utf-8">
<title>Brightpath EAP Flyer</title>
<link href="https://fonts.googleapis.com/css2?family=Open+Sans:wght@400;600;700&family=Roboto:wght@300;400&display=swap" rel="stylesheet">
<style>
  :root {
    --page-bg: #e6d5c9;
    --paper: #f1f0ee;
    --charcoal: #575454;
    --charcoal-dark: #454242;
    --tan: #cfa98d;
    --green: #5d8a6c;
    --ink: #4a4a4a;
    --white: #ffffff;
  }
  * { box-sizing: border-box; margin: 0; padding: 0; }
  html, body { width: 1200px; height: 800px; overflow: hidden; }
  body { background: var(--page-bg); font-family: "Roboto", Arial, sans-serif; }

  .flyer {
    position: absolute; left: 330px; top: 18px;
    width: 540px; height: 764px;
    background: var(--paper);
    overflow: hidden;
    box-shadow: 0 6px 24px rgba(0,0,0,.18);
  }
  .flyer__header { position: absolute; inset: 0 0 auto 0; height: 290px; }
  .flyer__header svg { display: block; }

  .flyer__title {
    position: absolute; left: 32px; top: 22px;
    font-family: "Open Sans", Arial, sans-serif; color: var(--white);
  }
  .flyer__title h1 { font-size: 32px; font-weight: 600; line-height: 1.05; }
  .flyer__title p { font-size: 12px; font-weight: 600; margin-top: 6px; }

  .contact { position: absolute; left: 32px; top: 124px; color: var(--white); font-family: "Open Sans", Arial, sans-serif; }
  .contact__phone { display: flex; align-items: center; }
  .contact__icon {
    width: 22px; height: 22px; border-radius: 50%; background: var(--green);
    border: 1.5px solid var(--white); display: flex; align-items: center; justify-content: center;
    position: relative; z-index: 1;
  }
  .contact__number {
    background: var(--tan); font-size: 14px; padding: 1px 28px 1px 14px;
    margin-left: -8px; border-radius: 0 12px 12px 0;
  }
  .contact__email { font-size: 14px; margin: 3px 0 0 18px; line-height: 1.3; }
  .contact__lines { font-size: 10px; margin-left: 18px; line-height: 1.45; }
  .contact__lines .org { font-size: 12.5px; }

  .brand {
    position: absolute; right: 26px; top: 232px;
    display: flex; align-items: center; gap: 8px;
    font-family: "Open Sans", Arial, sans-serif; font-weight: 600;
    font-size: 24px; color: var(--charcoal-dark);
  }
  .brand__dot { width: 14px; height: 14px; border-radius: 50%; background: var(--green); }

  .content { position: absolute; left: 0; right: 0; top: 278px; padding-right: 34px; }
  .section-title {
    display: inline-block; background: var(--tan); color: var(--white);
    font-family: "Open Sans", Arial, sans-serif; font-size: 12px; font-weight: 600;
    line-height: 17px; padding: 0 22px 0 36px; border-radius: 0 9px 9px 0; margin-top: 5px;
  }
  .section-body {
    font-size: 8.2px; font-weight: 300; color: var(--ink); line-height: 1.35;
    padding: 2px 0 0 36px;
  }
  .lead { color: var(--green); font-family: "Open Sans", Arial, sans-serif; font-size: 10.5px; padding: 2px 0 2px 30px; }

  .checklist { display: flex; gap: 60px; padding-left: 44px; }
  .checklist ul { list-style: none; }
  .checklist li {
    display: flex; align-items: center; gap: 7px;
    font-size: 8.2px; font-weight: 300; color: var(--ink); line-height: 1.5;
  }
  .checklist__col--right { padding-top: 14px; }

  .flyer__footer { position: absolute; left: 0; right: 0; bottom: 0; height: 10px; background: var(--green); }
</style>
</head>
<body>
<article class="flyer">
  <header class="flyer__header">
    <svg width="540" height="290" viewBox="0 0 540 290">
      <defs>
        <clipPath id="band-shape">
          <path d="M0 0 H540 V118 L210 262 Q192 270 174 267 L0 248 Z"/>
        </clipPath>
        <linearGradient id="hands-tone" x1="0" y1="0" x2="1" y2="1">
          <stop offset="0" stop-color="#4f4c4c"/>
          <stop offset=".55" stop-color="#5e5a5a"/>
          <stop offset="1" stop-color="#4a4747"/>
        </linearGradient>
      </defs>
      <g clip-path="url(#band-shape)">
        <rect width="540" height="290" fill="url(#hands-tone)" role="img" aria-label="Monochrome photograph of hands reaching towards each other"/>
      </g>
      <path d="M0 248 L174 267 Q192 270 210 262 L540 118" fill="none" stroke="#3e3b3b" stroke-width="3"/>
    </svg>

    <div class="flyer__title">
      <h1>Employee Assistance<br>Program (EAP)</h1>
      <p>Counselling for Work Related or Personal Issues</p>
    </div>

    <div class="contact">
      <div class="contact__phone">
        <span class="contact__icon">
          <svg width="12" height="12" viewBox="0 0 24 24"><path fill="#fff" d="M6.6 10.8a15.1 15.1 0 0 0 6.6 6.6l2.2-2.2a1 1 0 0 1 1-.25 11.4 11.4 0 0 0 3.6.57 1 1 0 0 1 1 1V20a1 1 0 0 1-1 1A17 17 0 0 1 3 4a1 1 0 0 1 1-1h3.5a1 1 0 0 1 1 1c0 1.25.2 2.45.57 3.57a1 1 0 0 1-.25 1z"/></svg>
        </span>
        <span class="contact__number">03 5550 1827</span>
      </div>
      <p class="contact__email">clinic@brightpath.example</p>
      <div class="contact__lines">
        <p class="org">Brightpath</p>
        <p>Harbourview House</p>
        <p>42 Elmwood Ave, Fairfield VIC 3078</p>
        <p>brightpath.example</p>
      </div>
    </div>
  </header>

  <div class="brand"><span class="brand__dot"></span>Brightpath</div>

  <main class="content">
    <h2 class="section-title">Employee Assistance Program</h2>
    <p class="section-body">Employee Assistance Program (EAP) is a confidential employer-funded support service available to employees and immediate family members experiencing personal or work-related concerns. Immediate family include your spouse, partner, children or others living in your household.</p>

    <h2 class="section-title">Counselling Services</h2>
    <p class="lead">EAP is provided for a variety of personal, emotional and work-related matters including:</p>
    <div class="checklist">
      <ul class="checklist__col">
        <li><svg width="9" height="9" viewBox="0 0 10 10"><rect x=".5" y="1.5" width="8" height="8" fill="none" stroke="#cfa98d"/><path d="M2 5l2 2 5-6" fill="none" stroke="#cfa98d" stroke-width="1.3"/></svg>Anxiety</li>
        <li><svg width="9" height="9" viewBox="0 0 10 10"><rect x=".5" y="1.5" width="8" height="8" fill="none" stroke="#cfa98d"/><path d="M2 5l2 2 5-6" fill="none" stroke="#cfa98d" stroke-width="1.3"/></svg>Depression and emotional wellbeing</li>
        <li><svg width="9" height="9" viewBox="0 0 10 10"><rect x=".5" y="1.5" width="8" height="8" fill="none" stroke="#cfa98d"/><path d="M2 5l2 2 5-6" fill="none" stroke="#cfa98d" stroke-width="1.3"/></svg>Workplace conflict or disharmony</li>
        <li><svg width="9" height="9" viewBox="0 0 10 10"><rect x=".5" y="1.5" width="8" height="8" fill="none" stroke="#cfa98d"/><path d="M2 5l2 2 5-6" fill="none" stroke="#cfa98d" stroke-width="1.3"/></svg>Coping with organisational change</li>
        <li><svg width="9" height="9" viewBox="0 0 10 10"><rect x=".5" y="1.5" width="8" height="8" fill="none" stroke="#cfa98d"/><path d="M2 5l2 2 5-6" fill="none" stroke="#cfa98d" stroke-width="1.3"/></svg>Stress and burnout</li>
        <li><svg width="9" height="9" viewBox="0 0 10 10"><rect x=".5" y="1.5" width="8" height="8" fill="none" stroke="#cfa98d"/><path d="M2 5l2 2 5-6" fill="none" stroke="#cfa98d" stroke-width="1.3"/></svg>Bullying</li>
        <li><svg width="9" height="9" viewBox="0 0 10 10"><rect x=".5" y="1.5" width="8" height="8" fill="none" stroke="#cfa98d"/><path d="M2 5l2 2 5-6" fill="none" stroke="#cfa98d" stroke-width="1.3"/></svg>Sexual harassment</li>
        <li><svg width="9" height="9" viewBox="0 0 10 10"><rect x=".5" y="1.5" width="8" height="8" fill="none" stroke="#cfa98d"/><path d="M2 5l2 2 5-6" fill="none" stroke="#cfa98d" stroke-width="1.3"/></svg>Self-esteem</li>
      </ul>
      <ul class="checklist__col checklist__col--right">
        <li><svg width="9" height="9" viewBox="0 0 10 10"><rect x=".5" y="1.5" width="8" height="8" fill="none" stroke="#cfa98d"/><path d="M2 5l2 2 5-6" fill="none" stroke="#cfa98d" stroke-width="1.3"/></svg>Reactions to traumatic or distressing events</li>
        <li><svg width="9" height="9" viewBox="0 0 10 10"><rect x=".5" y="1.5" width="8" height="8" fill="none" stroke="#cfa98d"/><path d="M2 5l2 2 5-6" fill="none" stroke="#cfa98d" stroke-width="1.3"/></svg>Critical incidents</li>
        <li><svg width="9" height="9" viewBox="0 0 10 10"><rect x=".5" y="1.5" width="8" height="8" fill="none" stroke="#cfa98d"/><path d="M2 5l2 2 5-6" fill="none" stroke="#cfa98d" stroke-width="1.3"/></svg>Grief and bereavement</li>
        <li><svg width="9" height="9" viewBox="0 0 10 10"><rect x=".5" y="1.5" width="8" height="8" fill="none" stroke="#cfa98d"/><path d="M2 5l2 2 5-6" fill="none" stroke="#cfa98d" stroke-width="1.3"/></svg>Substance misuse</li>
        <li><svg width="9" height="9" viewBox="0 0 10 10"><rect x=".5" y="1.5" width="8" height="8" fill="none" stroke="#cfa98d"/><path d="M2 5l2 2 5-6" fill="none" stroke="#cfa98d" stroke-width="1.3"/></svg>Domestic violence</li>
        <li><svg width="9" height="9" viewBox="0 0 10 10"><rect x=".5" y="1.5" width="8" height="8" fill="none" stroke="#cfa98d"/><path d="M2 5l2 2 5-6" fill="none" stroke="#cfa98d" stroke-width="1.3"/></svg>Interpersonal relationships</li>
        <li><svg width="9" height="9" viewBox="0 0 10 10"><rect x=".5" y="1.5" width="8" height="8" fill="none" stroke="#cfa98d"/><path d="M2 5l2 2 5-6" fill="none" stroke="#cfa98d" stroke-width="1.3"/></svg>Schooling and study difficulties</li>
      </ul>
    </div>

    <h2 class="section-title">Who Pays for the Service?</h2>
    <p class="section-body">Your employer will pay for an agreed number of sessions. You are not required to pay for using the Brightpath EAP service. The number of available sessions depends on the agreement we have with your employer.</p>

    <h2 class="section-title">Is it Confidential?</h2>
    <p class="section-body">Confidentiality is assured and maintained. All discussions with a clinician remain strictly confidential. Clinicians are bound by a professional code of ethics, preventing them giving out personal details without your written consent. In some cases, it may be helpful for the clinician to hold a discussion with a particular person in your workplace, like your manager. This would only occur with your written consent. Confidentiality and limitations of confidentiality are explained to employees at the beginning of the counselling process.</p>

    <h2 class="section-title">How do I make an EAP Appointment</h2>
    <p class="section-body">The Brightpath intake team are trained in handling distressing incidents and will assist in making your initial appointment. We will respond to your call and book your initial appointment as soon as possible at a time convenient to you.</p>

    <h2 class="section-title">About Brightpath</h2>
    <p class="section-body">Brightpath is a registered NDIS provider with significant experience working in the disability and mental health sectors so we understand your workplaces and the issues that might arise. We provide a confidential and effective counselling process that is solution-focused and practical. The service is aimed at enhancing wellbeing and mental health, and can be accessed via face-to-face consultations, and by Telehealth or phone. Accessing assistance is an act of independence and strength which can empower you to make positive changes in your life.</p>
  </main>

  <footer class="flyer__footer"></footer>
</article>
</body>
</html>
```